TR Advisory Business Cards - High End AV / Low Voltage Company

We are low voltage AV company that specializes in high end clients on the residential side and larger businesses on the commercial side. We want something modern, tech looking but also something that is extremely professional looking. We have uploaded our logos and postcards we already have in the field. Along with a picture of one of our wrapped vans. Our website is at www.trvadvisory.example and our primary colors are the orange, green, grey and blue all military color finishes.

We are interesting in the slogans "Pairing You with the Right Technology" or "Connecting the Coast with Tech"

Target Market(s)

We focus on 70% Commercial and 30% Residential Customers

Industry/Entity Type

Low Voltage, AV Company

Contact Information for Business Card

Name - Dorian Fairweather, Title - Owner, Office Phone - 555-714-3096, Mobile Phone - 555-802-4173, E-Mail - d@trvadvisory.example, Website: www.trvadvisory.example

Font styles to use
Sans Serif

Requirements
Must have
• Must have Name, Title, Work Phone & Mobile, Website and Logo.
Nice to have
• We want something that will impress our higher end clients with a great logo
Should not have
• Too traditional or plain.

```html
<!DOCTYPE html>
<html lang="en">
<head>
<meta charset="utf-8">
<title>TR Advisory Business Cards</title>
<link href="https://fonts.googleapis.com/css2?family=Montserrat:wght@400;500;600;700&display=swap" rel="stylesheet">
<style>
  :root {
    --backdrop: #2a2a2a;
    --card: #161616;
    --orange: #e8672f;
    --text: #f2f2f2;
    --emboss: #3c3c3c;
  }
  * { margin: 0; padding: 0; box-sizing: border-box; }
  html, body { width: 1200px; height: 1059px; overflow: hidden; }
  body {
    background: var(--backdrop);
    font-family: "Montserrat", sans-serif;
    position: relative;
  }
  .card {
    position: absolute;
    background: var(--card);
    box-shadow: 0 10px 24px rgba(0,0,0,0.55);
  }
  .card-front { left: 256px; top: 89px; width: 688px; height: 390px; }
  .card-back { left: 252px; top: 546px; width: 696px; height: 395px; }

  .front-wordmark {
    position: absolute; left: 0; right: 0; top: 150px;
    text-align: center;
    font-weight: 700; font-size: 54px; letter-spacing: 1px;
    color: var(--emboss);
  }
  .tagline {
    position: absolute; left: 0; right: 0;
    text-align: center;
    font-size: 18.5px; font-weight: 500; color: var(--text);
    white-space: nowrap;
  }
  .card-front .tagline { top: 342px; }
  .card-back .tagline { top: 344px; }

  .back-wordmark {
    position: absolute; left: 60px; width: 252px; top: 180px;
    text-align: center;
    font-weight: 600; font-size: 31px; color: var(--orange);
    white-space: nowrap;
  }
  .divider {
    position: absolute; left: 331px; top: 101px;
    width: 2px; height: 193px; background: var(--orange);
  }
  .person-name {
    position: absolute; left: 359px; top: 100px;
    font-weight: 700; font-size: 27px; color: var(--orange);
    white-space: nowrap;
  }
  .person-title {
    position: absolute; left: 359px; top: 136px;
    font-size: 18px; font-weight: 500; color: var(--text);
  }
  .contact-list {
    position: absolute; left: 359px; top: 190px;
    list-style: none;
  }
  .contact-item {
    display: flex; align-items: center;
    height: 27.5px;
    font-size: 18px; font-weight: 500; color: var(--text);
    white-space: nowrap;
  }
  .contact-icon { width: 14px; height: 14px; margin-right: 10px; fill: var(--orange); flex: none; }
</style>
</head>
<body>
  <section class="card card-front">
    <div class="front-wordmark">TR Advisory</div>
    <p class="tagline">Connecting the Coast with Tech</p>
  </section>

  <section class="card card-back">
    <div class="back-wordmark">TR Advisory</div>
    <div class="divider"></div>
    <h1 class="person-name">Dorian Fairweather</h1>
    <p class="person-title">Owner</p>
    <ul class="contact-list">
      <li class="contact-item">
        <svg class="contact-icon" viewBox="0 0 16 16"><path d="M1 6c0-2 3-3 7-3s7 1 7 3v1h-3.5V5.5h-7V7H1z"/><path d="M3 8h10l1 6H2z"/></svg>
        555-714-3096
      </li>
      <li class="contact-item">
        <svg class="contact-icon" viewBox="0 0 16 16"><path d="M4 1h8v14H4zM5.3 2.5v9.5h5.4V2.5z"/><circle cx="8" cy="13.5" r="0.8"/></svg>
        555-802-4173
      </li>
      <li class="contact-item">
        <svg class="contact-icon" viewBox="0 0 16 16"><path d="M1 3.5h14v1.2L8 9 1 4.7z"/><path d="M1 6.3l7 4.3 7-4.3V12.5H1z"/></svg>
        d@trvadvisory.example
      </li>
      <li class="contact-item">
        <svg class="contact-icon" viewBox="0 0 16 16"><circle cx="8" cy="8" r="6.3" fill="none" stroke="#e8672f" stroke-width="1.4"/><path d="M1.7 7.3h12.6v1.4H1.7z"/><ellipse cx="8" cy="8" rx="2.6" ry="6.3" fill="none" stroke="#e8672f" stroke-width="1.3"/></svg>
        www.trvadvisory.example
      </li>
    </ul>
    <p class="tagline">Connecting the Coast with Tech</p>
  </section>
</body>
</html>
```